public page walrus GX (www.walrusgx.com)

https://www.quillbarn.net/shard/s412/sh/a3b1c9d2-58e4-4f7a-b2c6-1d9e0f7a3b45/41c7e2a9d08b6f53e17a92c4d6b0f831

compatible with wordpress

Designs look the same

Industry/Entity Type

Finance And Accounting

Coding

Coded - Design and coding required

Number of Pages Required

1 page

Font styles to use
Sans Serif

Colors
85cae6
3176b5
cfdeed
fac994
fff3d1
fefdec
cfcfcf
e8e8e8
9d9d9d

```html
<!DOCTYPE html>
<html lang="en">
<head>
<meta charset="utf-8">
<title>walrus GX</title>
<link href="https://fonts.googleapis.com/css2?family=Roboto:wght@300;400;500&display=swap" rel="stylesheet">
<style>
:root{
  --orange:#f7861c;
  --blue:#3176b5;
  --blue-bright:#1f6fd0;
  --blue-deep:#0b2fa8;
  --sky:#85cae6;
  --pale-blue:#cfdeed;
  --grey-1:#e8e8e8;
  --grey-2:#cfcfcf;
  --grey-3:#9d9d9d;
  --ink:#333333;
  --body:#666666;
  --white:#ffffff;
  --footer:#eef0f2;
}
*{margin:0;padding:0;box-sizing:border-box}
html,body{width:1200px;height:3285px;overflow:hidden}
body{font-family:'Roboto',Arial,sans-serif;color:var(--ink);background:var(--white)}
.page{position:relative;width:1200px;height:3285px;overflow:hidden}
.abs{position:absolute}

/* hero */
.hero{left:0;top:0;width:1200px;height:683px;background:linear-gradient(120deg,#5d6e80 0%,#3d4e62 45%,#25303e 100%)}
.brand{left:180px;top:36px;display:flex;align-items:center;gap:12px;color:var(--white);font-size:26px;font-weight:500;letter-spacing:.5px}
.brand-dot{width:42px;height:42px;border-radius:50%;background:var(--white)}
.nav{left:448px;top:46px;display:flex;gap:27px;color:var(--white);font-size:13px;text-transform:uppercase}
.btn-nav{top:40px;height:30px;color:var(--white);font-size:12px;text-transform:uppercase;display:flex;align-items:center;justify-content:center}
.btn-signup{left:856px;width:72px;background:#2d6fc4}
.btn-signin{left:937px;width:76px;background:var(--orange)}
.hero-title{left:0;width:1200px;top:262px;text-align:center;color:var(--white);font-weight:300;font-size:50px;letter-spacing:3px}
.hero-sub{left:0;width:1200px;top:326px;text-align:center;color:var(--white);font-weight:300;font-size:23px}
.email{left:318px;top:385px;width:368px;height:53px;border-radius:27px;background:var(--white);color:#555;font-size:13px;padding-left:28px;display:flex;align-items:center;text-transform:uppercase}
.cta{left:694px;top:385px;width:182px;height:53px;border-radius:27px;background:var(--orange);color:var(--white);font-weight:500;font-size:17px;display:flex;align-items:center;justify-content:center;text-transform:uppercase}
.dots{left:568px;top:638px;display:flex;gap:6px}
.dots span{width:10px;height:10px;border-radius:50%;background:var(--white)}
.dots span:first-child{background:transparent;border:2px solid var(--white)}

/* features */
.features-bg{left:0;top:1830px;width:1200px;height:240px;background:linear-gradient(180deg,#ffffff 0%,#f0f0f0 100%)}
.art{border-radius:48% 52% 46% 54%;background:radial-gradient(circle at 50% 45%,#eef1f6 0%,#e4e6ea 70%,#f3f3f3 100%)}
.art-money{border-radius:40%;background:radial-gradient(circle at 50% 40%,#cfe8f5 0%,#dfeefa 55%,#ffffff 90%)}
.feature h2{font-weight:300;font-size:31px;color:var(--ink);text-transform:uppercase;letter-spacing:.5px}
.feature p{font-size:13.5px;line-height:21px;color:var(--body);margin-top:14px;width:420px}
.feature p+p{margin-top:12px}
.btn-more{display:flex;align-items:center;justify-content:center;width:152px;height:47px;background:var(--orange);color:var(--white);font-size:17px;margin-top:22px}

/* pricing */
.price-lead{left:0;width:1200px;top:2148px;text-align:center;font-size:24px;font-weight:300;color:#555}
.price{left:0;width:1200px;top:2188px;text-align:center;font-size:52px;color:var(--blue-bright);font-weight:400}
.btn-price{left:508px;top:2278px;width:180px;height:44px;background:var(--orange);color:var(--white);font-size:17px;display:flex;align-items:center;justify-content:center}

/* faq */
.faq{left:0;top:2410px;width:1200px;height:476px;background:linear-gradient(100deg,#1a7fe0 0%,#0f4fc4 45%,#0a2aa0 100%)}
.faq-title{left:0;width:1200px;top:2446px;text-align:center;color:var(--white);font-size:40px;font-weight:300}
.faq-list{left:228px;top:2521px;width:742px}
.faq-item{background:var(--white);border-bottom:3px solid #1c54c0;height:44px;display:flex;align-items:center;justify-content:space-between;padding:0 22px 0 28px;font-size:15.5px;color:#444;margin-top:5px}
.faq-item.open{background:#2a85dd;color:var(--white);margin-top:0;border:none;height:46px}
.faq-answer{background:var(--white);padding:14px 28px;font-size:12.5px;line-height:20px;color:#888;height:101px}

/* footer */
.footer{left:0;top:2886px;width:1200px;height:338px;background:var(--footer)}
.foot-brand{left:182px;top:2960px;display:flex;align-items:center;gap:10px;color:var(--blue);font-size:30px;font-weight:400}
.foot-brand-dot{width:34px;height:34px;border-radius:50%;background:var(--orange)}
.foot-col h4{font-weight:400;font-size:18px;color:#333}
.foot-col ul{list-style:none;margin-top:17px}
.foot-col li{font-size:13px;color:#444;height:27.5px}
.socials{display:flex;gap:7px;margin-top:14px}
.socials span{width:28px;height:28px;border-radius:50%;border:2px solid #333}
.copyright{left:0;top:3224px;width:1200px;height:61px;border-top:1px solid var(--grey-2);background:var(--footer);text-align:center;font-size:13px;color:#666;padding-top:20px}
</style>
</head>
<body>
<div class="page">

  <header class="abs hero" role="img" aria-label="Photo of a person working on a laptop beside financial charts and glasses"></header>
  <div class="abs brand"><span class="brand-dot"></span>walrus GX</div>
  <nav class="abs nav"><span>Home</span><span>Pricing</span><span>About Us</span><span>Contact</span><span>Blog</span><span>FAQ</span></nav>
  <div class="abs btn-nav btn-signup">Sign Up</div>
  <div class="abs btn-nav btn-signin">Sign In</div>
  <h1 class="abs hero-title">WELCOME TO WALRUS GX</h1>
  <p class="abs hero-sub">Vivamus porttitor purus nisi eleifend libero a tempus</p>
  <div class="abs email">Enter your email</div>
  <div class="abs cta">Get Started</div>
  <div class="abs dots"><span></span><span></span><span></span><span></span></div>

  <div class="abs features-bg"></div>

  <div class="abs art" style="left:153px;top:734px;width:395px;height:350px" role="img" aria-label="Illustration of a monitor showing a candlestick chart"></div>
  <section class="abs feature" style="left:596px;top:800px">
    <h2>Calculate your profit</h2>
    <p>Mauris vel lacus vitae felis vestibulum volutpat Etiam est nunc venenatis in tristique eu imperdiet ac nisl</p>
    <p>Cum sociis natoque penatibus et magnis dis parturient montes nascetur ridiculus mus In iaculis facilisis massa Etiam eu urna Sed porta Suspendisse quam leo molestie sed luctus quis feugiat in pede Fusce tellus Sed metus augue convallis et v</p>
    <div class="btn-more">Learn More</div>
  </section>

  <section class="abs feature" style="left:182px;top:1222px">
    <h2>Why choose us</h2>
    <p>Mauris vel lacus vitae felis vestibulum volutpat Etiam est nunc venenatis in tristique eu imperdiet ac nisl</p>
    <p>Cum sociis natoque penatibus et magnis dis parturient montes nascetur ridiculus mus In iaculis facilisis massa Etiam eu urna Sed porta Suspendisse quam leo molestie sed luctus quis feugiat in pede Fusce tellus Sed metus augue convallis et v</p>
    <div class="btn-more">Learn More</div>
  </section>
  <div class="abs art" style="left:657px;top:1183px;width:340px;height:295px" role="img" aria-label="Illustration of a computer mouse with a cable"></div>

  <div class="abs art-money" style="left:164px;top:1620px;width:373px;height:330px" role="img" aria-label="Illustration of a money bag with coins and sparkles"></div>
  <section class="abs feature" style="left:613px;top:1630px">
    <h2>How to calculate</h2>
    <p>Mauris vel lacus vitae felis vestibulum volutpat Etiam est nunc venenatis in tristique eu imperdiet ac nisl</p>
    <p>Cum sociis natoque penatibus et magnis dis parturient montes nascetur ridiculus mus In iaculis facilisis massa Etiam eu urna Sed porta Suspendisse quam leo molestie sed luctus quis feugiat in pede Fusce tellus Sed metus augue convallis et v</p>
    <div class="btn-more">Learn More</div>
  </section>

  <p class="abs price-lead">Morbi diam mauris viverra in gravida eu mattis ante</p>
  <p class="abs price">$4.95/month*</p>
  <div class="abs btn-price">Get Started Now</div>

  <section class="abs faq" role="img" aria-label="Blue background with a network of connected dots"></section>
  <h2 class="abs faq-title">FAQ</h2>
  <div class="abs faq-list">
    <div class="faq-item open">Ait amet porttitor mattis enim In massa libero interdum
      <svg width="16" height="10" viewBox="0 0 16 10"><path d="M1 1l7 7 7-7" fill="none" stroke="#fff" stroke-width="2"/></svg></div>
    <div class="faq-answer">Ait amet porttitor mattis enim In massa libero interdum nec interdum vel blandit sed nulla In ullamcorper est eget tempor cursus neque mi consectetuer mi a ultricies massa est sed nisl Class aptent taciti sociosqu ad litora torquent per conubia nostra per inceptos hymenaeos Proin nulla arcu nonummy</div>
    <div class="faq-item">Nec interdum vel blandit sed nulla In ullamcorper est
      <svg width="16" height="10" viewBox="0 0 16 10"><path d="M1 1l7 7 7-7" fill="none" stroke="#888" stroke-width="2"/></svg></div>
    <div class="faq-item">Eget tempor cursus neque mi consectetuer mi a ultricies massa
      <svg width="16" height="10" viewBox="0 0 16 10"><path d="M1 1l7 7 7-7" fill="none" stroke="#888" stroke-width="2"/></svg></div>
    <div class="faq-item">Sst sed nisl Class aptent taciti sociosqu ad litora
      <svg width="16" height="10" viewBox="0 0 16 10"><path d="M1 1l7 7 7-7" fill="none" stroke="#888" stroke-width="2"/></svg></div>
  </div>

  <footer class="abs footer"></footer>
  <div class="abs foot-brand"><span class="foot-brand-dot"></span>walrus GX</div>
  <div class="abs foot-col" style="left:405px;top:2940px"><h4>Company</h4><ul><li>Home</li><li>Pricing</li><li>About Us</li><li>Contact</li><li>Blog</li></ul></div>
  <div class="abs foot-col" style="left:565px;top:2940px"><h4>Resources</h4><ul><li>FAQs</li><li>Login</li><li>Sign Up</li><li>Privacy &amp; Terms</li></ul></div>
  <div class="abs foot-col" style="left:731px;top:2940px"><h4>Sublinks</h4><ul><li>Lorem ipsum</li><li>Dolor sit</li><li>Amet consectet</li><li>Adipiscing elit</li><li>Nam cursus</li></ul></div>
  <div class="abs foot-col" style="left:863px;top:2940px"><h4>Follow Us</h4><div class="socials"><span></span><span></span><span></span><span></span></div></div>
  <div class="abs copyright">© 2018 Company Name&nbsp; All right reserved&nbsp; Term of Use</div>

</div>
</body>
</html>
```